Business Card Design Project

Recently had a new logo made up for my company and new business cards done as well. I have attached the logos for your viewing. Additional projects may be needed. Good luck!

Business

```html
<!DOCTYPE html>
<html lang="en">
<head>
<meta charset="utf-8">
<title>Whitcombe Financial Group – Business Card</title>
<link rel="stylesheet" href="https://fonts.googleapis.com/css2?family=Ubuntu:wght@400;500&family=Jura:wght@500&display=swap">
<style>
  :root {
    --backdrop: #e4e4e4;
    --card: #22232b;
    --gold: #c9b88a;
    --white: #ffffff;
    --blue: #29a8e0;
  }
  * { margin: 0; padding: 0; box-sizing: border-box; }
  html, body { width: 1200px; height: 1000px; overflow: hidden; }
  body { background: var(--backdrop); position: relative; font-family: "Ubuntu", sans-serif; }

  .card {
    position: absolute; left: 206px; width: 812px; height: 464px;
    background: var(--card); border-radius: 10px; overflow: hidden;
  }
  .card--front { top: 20px; }
  .card--back { top: 517px; }

  .tab { position: absolute; width: 17px; }
  .tab--left { left: 0; }
  .tab--right { right: 0; }
  .tab--white { background: var(--white); }
  .tab--gold { background: var(--gold); }
  .card--front .tab--white { top: 205px; height: 90px; }
  .card--front .tab--gold { top: 302px; height: 106px; }
  .card--back .tab--white { top: 228px; height: 90px; }
  .card--back .tab--gold { top: 325px; height: 108px; }

  .brand {
    position: absolute; display: flex; flex-direction: column; align-items: center;
    color: var(--gold); font-family: "Ubuntu", sans-serif; font-weight: 500;
    text-transform: uppercase; text-align: center;
  }
  .brand__mark { width: 46px; height: 46px; background: var(--gold); margin-bottom: 26px; }
  .brand__name { font-size: 50px; letter-spacing: 3px; line-height: 1; }
  .brand__sub { font-size: 28px; letter-spacing: 3px; line-height: 1; margin-top: 14px; }
  .card--front .brand { left: 30px; top: 120px; width: 320px; }
  .card--back .brand { left: 0; right: 0; top: 110px; }

  .contact { position: absolute; left: 375px; top: 30px; color: var(--white); }
  .contact__name { font-size: 26px; font-weight: 500; line-height: 1.2; }
  .contact__role { font-size: 26px; font-weight: 500; color: var(--blue); line-height: 1.2; }
  .contact__list { list-style: none; margin-top: 66px; font-size: 20px; line-height: 1.2; }
  .contact__list li { margin-bottom: 12px; }
  .contact__list .label { color: var(--blue); }
  .contact__list .address { margin-bottom: 0; }

  .web {
    position: absolute; left: 388px; top: 412px; display: flex; align-items: center; gap: 14px;
    color: var(--gold); font-size: 21px; font-weight: 500;
  }

  .tagline {
    position: absolute; left: 0; right: 0; top: 314px; text-align: center;
    font-family: "Jura", sans-serif; font-weight: 500; font-size: 33px;
    color: var(--gold); letter-spacing: 0.5px;
  }
</style>
</head>
<body>

<section class="card card--front">
  <span class="tab tab--left tab--white"></span>
  <span class="tab tab--left tab--gold"></span>
  <span class="tab tab--right tab--white"></span>
  <span class="tab tab--right tab--gold"></span>

  <div class="brand">
    <span class="brand__mark"></span>
    <span class="brand__name">Whitcombe</span>
    <span class="brand__sub">Financial Group</span>
  </div>

  <div class="contact">
    <p class="contact__name">Daniel R. Whitcombe</p>
    <p class="contact__role">Director</p>
    <ul class="contact__list">
      <li><span class="label">E:</span> Dwhitcombe@whitcombefin.com</li>
      <li><span class="label">P:</span> 516-555-0142 <span class="label">F:</span> 516-555-0187</li>
      <li class="address">4200 Meadowbrook Road, Suite 310E<br>Glen Harbor, New York 11790</li>
    </ul>
  </div>

  <div class="web">
    <svg width="40" height="40" viewBox="0 0 40 40" aria-hidden="true">
      <circle cx="20" cy="20" r="19" fill="#2f8fd4"/>
      <path d="M8 12c5-2 8 2 7 6s-5 4-4 9c1 3 0 6-3 4-4-4-6-13 0-19z" fill="#4caf50"/>
      <path d="M22 6c4 0 9 4 10 8-3 1-5-1-7 2s2 6 0 10c-2 3-5 1-5-3s-3-6-1-10c1-3 0-7 3-7z" fill="#4caf50"/>
    </svg>
    <span>www.whitcombefin.com</span>
  </div>
</section>

<section class="card card--back">
  <span class="tab tab--left tab--white"></span>
  <span class="tab tab--left tab--gold"></span>
  <span class="tab tab--right tab--white"></span>
  <span class="tab tab--right tab--gold"></span>

  <div class="brand">
    <span class="brand__mark"></span>
    <span class="brand__name">Whitcombe</span>
    <span class="brand__sub">Financial Group</span>
  </div>

  <p class="tagline">Estate Planning and Insurance Specialist</p>
</section>

</body>
</html>
```